Asphalt Paving Specialists Business Cards

Our company is TREVIN ASPHALT. We need a business cards two of our asphalt paving team members. We're asphalt specialists.
I need two made up please. The details on the front of the each business card i would like please is as follows.
Address is 87 Marrowby St, Delvane, QLD, 4187.

Company Director
Gordon Pelliway
gord@trevinpave.com.au
04 58 736 042
www.trevinpave.com.au

Supervisor
Curtis Vonnegard
curtis@trevinpave.com.au
0462 873 105
www.trevinpave.com.au

We do all aspects of Asphalt Paving. Specific Services include - Driveways, Carparks & sub-divisions. All Roads. Repairs and Maintenance.

We provide free quotes!

I dont have a certain way i want them to look so im open to all designs :)

** I have uploaded our logo for the TREVIN ASPHALT. HOWEVER, CAN YOU PLEASE GET RID OF THE ( PTY LTD )

Thank you
Renata Fulch
TREVIN ASPHALT

Target Market(s)

Home owners and Business Owners

Contact Information for Business Card

Asphalt Paving Specialists. All aspects of Asphalt. Residential, Commercial & Industrial. Based in Brisbane.

Font styles to use
Sans Serif

Colors

Designer to choose colors to be used in the design.

Requirements
Nice to have
• maybe an image of a driveway? or Asphalt?

```html
<!DOCTYPE html>
<html lang="en">
<head>
<meta charset="utf-8">
<title>Trevin Asphalt – Business Card</title>
<link rel="stylesheet" href="https://fonts.googleapis.com/css2?family=Roboto+Condensed:wght@400;700&family=Lato:wght@400&family=Cormorant+Garamond:ital,wght@1,500&display=swap">
<style>
  :root {
    --backdrop: #2d2d2e;
    --card-white: #ffffff;
    --brand-blue: #38b3e6;
    --ink: #1a1a1a;
    --ink-navy: #0f2233;
    --rule: #9a9a9a;
    --rule-soft: #dddddd;
    --sky-top: #8fd5f1;
    --sky-bottom: #14abe1;
  }
  * { margin: 0; padding: 0; box-sizing: border-box; }
  html, body { width: 1200px; height: 1200px; overflow: hidden; }
  body { background: var(--backdrop); position: relative; font-family: "Lato", Arial, sans-serif; color: var(--ink); }

  .card { position: absolute; top: 310px; height: 594px; text-align: center; }
  .card--front { left: 234px; width: 364px; background: var(--card-white); }
  .card--back { left: 627px; width: 369px; background: linear-gradient(180deg, var(--sky-top) 0%, var(--sky-bottom) 100%); color: var(--ink-navy); }

  .brand { position: absolute; top: 160px; left: 0; right: 0; display: flex; align-items: center; justify-content: center; gap: 10px; }
  .brand__dot { width: 18px; height: 18px; border-radius: 50%; background: var(--ink); }
  .brand__name { font-family: "Roboto Condensed", Arial, sans-serif; font-weight: 700; font-size: 34px; letter-spacing: 1px; color: var(--ink); }

  .person { position: absolute; top: 330px; left: 0; right: 0; }
  .person__name { font-family: "Roboto Condensed", Arial, sans-serif; font-size: 22px; color: var(--brand-blue); line-height: 24px; }
  .person__role { font-size: 17px; line-height: 20px; }

  .contact-icons { position: absolute; top: 384px; left: 87px; right: 87px; display: flex; align-items: center; gap: 4px; }
  .contact-icons__rule { flex: 1; height: 1px; background: var(--rule); }
  .contact-icons svg { width: 24px; height: 24px; display: block; }

  .contact { position: absolute; top: 419px; left: 0; right: 0; font-size: 17px; line-height: 22px; }
  .contact__rule { position: absolute; top: 494px; left: 88px; right: 80px; height: 1px; background: var(--rule-soft); }
  .address { position: absolute; top: 506px; left: 0; right: 0; font-size: 17px; line-height: 22px; }

  .pitch { position: absolute; top: 178px; left: 0; right: 0; font-family: "Roboto Condensed", Arial, sans-serif; font-weight: 700; font-size: 31px; line-height: 38px; text-transform: uppercase; }
  .services { position: absolute; top: 286px; left: 0; right: 0; font-size: 19px; line-height: 24px; }
  .quote { position: absolute; top: 502px; left: 0; right: 0; font-family: "Cormorant Garamond", Georgia, serif; font-style: italic; font-weight: 500; font-size: 30px; }
</style>
</head>
<body>
  <section class="card card--front">
    <div class="brand">
      <span class="brand__dot"></span>
      <span class="brand__name">TREVIN ASPHALT</span>
    </div>

    <div class="person">
      <p class="person__name">GORDON PELLIWAY</p>
      <p class="person__role">Company Director</p>
    </div>

    <div class="contact-icons">
      <span class="contact-icons__rule"></span>
      <svg viewBox="0 0 24 24" aria-label="Phone">
        <circle cx="12" cy="12" r="12" fill="#38b3e6"/>
        <path d="M7 10.5c0-2 2.2-3 5-3s5 1 5 3v1h-2.5v-1.2h-5v1.2H7z M8 12.5h8l1 4H7z" fill="#fff"/>
      </svg>
      <svg viewBox="0 0 24 24" aria-label="Email">
        <circle cx="12" cy="12" r="12" fill="#38b3e6"/>
        <rect x="6.5" y="8" width="11" height="8" fill="#fff"/>
        <path d="M6.5 8l5.5 4.5L17.5 8" fill="none" stroke="#38b3e6" stroke-width="1"/>
      </svg>
      <svg viewBox="0 0 24 24" aria-label="Website">
        <circle cx="12" cy="12" r="12" fill="#38b3e6"/>
        <circle cx="12" cy="12" r="5.5" fill="#fff"/>
        <path d="M9.5 9.5q2 1 1.5 3t2.5 2.5" fill="none" stroke="#38b3e6" stroke-width="1.2"/>
      </svg>
      <span class="contact-icons__rule"></span>
    </div>

    <div class="contact">
      <p>04 58 736 042</p>
      <p>gord@trevinpave.com.au</p>
      <p>www.trevinpave.com.au</p>
    </div>
    <div class="contact__rule"></div>
    <div class="address">
      <p>87 Marrowby St</p>
      <p>Delvane, QLD, 4187</p>
    </div>
  </section>

  <section class="card card--back">
    <h2 class="pitch">We do all aspects of<br>asphalt paving</h2>
    <div class="services">
      <p>SPECIFIC SERVICES INCLUDE</p>
      <p>Driveways</p>
      <p>Carparks &amp; sub-divisions.</p>
      <p>All Roads. Repairs and Maintenance.</p>
    </div>
    <p class="quote">We provide free quotes!</p>
  </section>
</body>
</html>
```